Quillmere AI Corporate Presentation Deck

Create a new, updated presentation deck template based on the look and feel of our new website,
https://qlmr.ai. Please use the current capabilities presentation deck (attached) as placeholder for copy and
graphic elements but everything should be updated to better align with the updated website.

```html
<!DOCTYPE html>
<html lang="en">
<head>
<meta charset="utf-8">
<title>Quillmere AI – Capabilities Presentation 2026</title>
<link href="https://fonts.googleapis.com/css2?family=Poppins:wght@200;300;400;500;600;700&display=swap" rel="stylesheet">
<style>
  :root{
    --sheet:#b3b3b3;
    --slide:#141b26;
    --green:#1fd08f;
    --blue:#13a9ea;
    --deep:#1440a8;
    --white:#ffffff;
    --muted:#d9dee6;
    --grid:#3a4453;
  }
  *{margin:0;padding:0;box-sizing:border-box}
  html,body{width:857px;height:1200px;overflow:hidden}
  body{background:var(--sheet);font-family:"Poppins",sans-serif;color:var(--white);position:relative}
  .slide{position:absolute;width:329px;height:185px;background:var(--slide);overflow:hidden}
  .col-l{left:90px}.col-r{left:438px}
  .row-1{top:95px}.row-2{top:301px}.row-3{top:508px}.row-4{top:714px}.row-5{top:920px}
  .abs{position:absolute}
  .brand{position:absolute;display:flex;align-items:center;gap:2px;font-weight:600;color:var(--white);white-space:nowrap}
  .brand .dot{border-radius:50%;background:var(--white);display:inline-block}
  .brand-sm{left:14px;top:166px;font-size:5px}
  .brand-sm .dot{width:4px;height:4px}
  .heading{position:absolute;left:14px;top:14px;font-size:11px;line-height:13px;font-weight:700;color:var(--blue);white-space:nowrap}
  .glow{position:absolute;background:radial-gradient(circle at 55% 55%,rgba(31,208,143,.55),rgba(20,64,168,.55) 45%,rgba(20,27,38,0) 72%)}
  .body-copy{position:absolute;left:13px;top:36px;width:145px;font-size:4.2px;line-height:5.5px;font-weight:300;color:var(--muted);text-align:justify}
  .body-copy p{margin-bottom:4px}
  .frame{position:absolute;border:.6px solid var(--green);border-right-color:var(--deep);border-bottom-color:var(--deep);border-radius:4px}
  .chart-title{position:absolute;font-size:7px;font-weight:600;color:var(--green)}
  .legend{position:absolute;display:flex;gap:6px;font-size:3.4px;color:var(--muted)}
  .legend span{display:flex;align-items:center;gap:1.5px}
  .legend i{width:3.5px;height:3.5px;border-radius:50%;display:inline-block}
  svg text{font-family:"Poppins",sans-serif}

  .cover-title{left:19px;top:18px;font-size:18px;line-height:20px;font-weight:300}
  .cover-title .accent{color:var(--green);font-weight:200}
  .cover-meta{right:20px;top:17px;font-size:6.4px;line-height:7px;text-align:right;font-weight:300}
  .brand-lg{left:19px;top:150px;font-size:11px}
  .brand-lg .dot{width:9px;height:9px;margin-right:2px}

  .toc-title{left:17px;top:19px;font-size:14px;line-height:14px;font-weight:700}
  .toc-title span{color:var(--blue)}
  .toc-item{position:absolute;font-size:4.6px;font-weight:600}
  .toc-item small{display:block;font-size:3.8px;color:var(--white);font-weight:500;margin-top:1.5px}
  .toc-green{color:var(--green)}.toc-blue{color:var(--blue)}
  .pill{position:absolute;width:11px;height:96px;top:65px;border-radius:6px}
  .pill span{position:absolute;left:0;width:11px;text-align:center;font-size:3.8px;font-weight:500;color:var(--slide)}

  .side-copy{position:absolute;width:72px;font-size:4.1px;line-height:5.3px;font-weight:300;color:var(--muted)}
  .side-copy b{display:block;color:var(--green);font-weight:600}
  .intro-copy{position:absolute;left:13px;width:135px;font-size:5.1px;line-height:6px;font-weight:300;color:var(--muted)}

  .feature{position:absolute;left:226px;width:95px;font-size:5.2px;line-height:6.3px;font-weight:300}
  .feature b{display:block;color:var(--green);font-weight:600}
  .shot{position:absolute;left:173px;width:46px;border:.6px solid var(--green);border-radius:2px;background:linear-gradient(160deg,#1b2636,#0d1420)}

  .thanks{left:19px;top:48px;font-size:34px;line-height:31px;color:var(--green);font-weight:200}
  .thanks strong{font-weight:700}
  .thanks-meta{left:19px;top:146px;font-size:9px;line-height:9.5px;font-weight:300}
</style>
</head>
<body>

<!-- 1 Cover -->
<section class="slide col-l row-1">
  <h1 class="abs cover-title"><span class="accent">The AI Hub<br>for Data,</span><br>Sound, and<br>Intelligence</h1>
  <p class="abs cover-meta">CAPABILITIES<br>PRESENTATION<br>2026</p>
  <div class="glow" style="left:140px;top:30px;width:200px;height:170px" role="img" aria-label="Brand decoration area in green and blue tones"></div>
  <div class="brand brand-lg"><i class="dot"></i>Quillmere AI</div>
</section>

<!-- 2 Contents -->
<section class="slide col-r row-1">
  <div class="glow" style="left:70px;top:-20px;width:75px;height:60px" role="img" aria-label="Brand decoration area in green and blue tones"></div>
  <h2 class="abs toc-title">Table of<br><span>Contents</span></h2>
  <div class="toc-item toc-green" style="left:18px;top:68px">Welcome Slide<small>Write a Short Summary for this Slide</small></div>
  <div class="toc-item toc-green" style="left:18px;top:94px">About Us<small>Write a Short Summary for this Slide</small></div>
  <div class="toc-item toc-green" style="left:18px;top:119px">Mission &amp; Vision<small>Write a Short Summary for this Slide</small></div>
  <div class="toc-item toc-green" style="left:18px;top:145px">Our History<small>Write a Short Summary for this Slide</small></div>
  <div class="pill" style="left:146px;background:var(--green)"><span style="top:8px">01</span><span style="top:34px">02</span><span style="top:59px">03</span><span style="top:85px">04</span></div>
  <div class="toc-item toc-blue" style="left:170px;top:68px">Pricing Slide<small>Write a Short Summary for this Slide</small></div>
  <div class="toc-item toc-blue" style="left:170px;top:94px">Our Infographics<small>Write a Short Summary for this Slide</small></div>
  <div class="toc-item toc-blue" style="left:170px;top:119px">Client Reviews<small>Write a Short Summary for this Slide</small></div>
  <div class="toc-item toc-blue" style="left:170px;top:145px">Data &amp; Charts<small>Write a Short Summary for this Slide</small></div>
  <div class="pill" style="left:299px;background:var(--blue)"><span style="top:8px">05</span><span style="top:34px">06</span><span style="top:59px">07</span><span style="top:85px">08</span></div>
</section>

<!-- 3 Problem / Solution -->
<section class="slide col-l row-2">
  <h2 class="heading">The Problem</h2>
  <h2 class="heading" style="left:auto;right:14px;color:var(--green)">The Solution</h2>
  <div class="side-copy" style="left:13px;top:42px">Companies and institutions lack a process and platform for identifying, valuating, and monetizing core and derivative data assets.</div>
  <div class="side-copy" style="left:13px;top:79px">Organizations and governments have operational risk and lack of fiduciary control over data assets of all types.</div>
  <div class="side-copy" style="left:13px;top:112px">Corporations do not have a reliable source for minting cryptocurrencies, data-backed digital assets.</div>
  <svg class="abs" style="left:103px;top:29px" width="124" height="124" viewBox="0 0 124 124">
    <defs>
      <linearGradient id="ring" x1="0" y1="0" x2="1" y2="1"><stop offset="0" stop-color="#1440a8"/><stop offset="1" stop-color="#1fd08f"/></linearGradient>
      <linearGradient id="photo" x1="0" y1="0" x2="1" y2="1"><stop offset="0" stop-color="#2b4fb8"/><stop offset="1" stop-color="#0b1a55"/></linearGradient>
    </defs>
    <circle cx="62" cy="62" r="60" fill="none" stroke="url(#ring)" stroke-width="1.6"/>
    <circle cx="62" cy="62" r="55" fill="none" stroke="#1fd08f" stroke-width="1.6" stroke-dasharray="120 226"/>
    <path d="M62 12 A50 50 0 0 0 62 112 L62 86 A24 24 0 0 1 62 38 Z" fill="url(#photo)" role="img" aria-label="Abstract data visual in deep blue tones"/>
    <path d="M87 18.7 A50 50 0 0 1 109 44.9 L84.6 53.8 A24 24 0 0 0 74 41.2 Z" fill="#eef3f8"/>
    <path d="M109.6 46.5 A50 50 0 0 1 109.6 77.5 L84.8 69.4 A24 24 0 0 0 84.8 54.6 Z" fill="#eef3f8"/>
    <path d="M109 79.1 A50 50 0 0 1 87 105.3 L74 82.8 A24 24 0 0 0 84.6 70.2 Z" fill="#eef3f8"/>
  </svg>
  <div class="side-copy" style="right:14px;top:40px;width:70px;text-align:right">The patented Quillmere® platform transforms derivative data from a cost driver to a revenue producer with our novel 3-part system.</div>
  <div class="side-copy" style="right:14px;top:71px;width:70px;text-align:right"><b>Data Refinery</b>Index, categorize, and objectify data assets.</div>
  <div class="side-copy" style="right:14px;top:92px;width:75px;text-align:right"><b>Quillmere®</b>Get real-time valuation of data and dynamic visualization of data assets.</div>
  <div class="side-copy" style="right:14px;top:119px;width:75px;text-align:right"><b>Ledgerline Exchange®</b>Buy or sell data on the Ledgerline Exchange®. Automatically list your data assets in the top tier crypto and digital assets exchanges.</div>
  <div class="brand brand-sm"><i class="dot"></i>Quillmere AI</div>
</section>

<!-- 4 Product -->
<section class="slide col-r row-2">
  <h2 class="heading">Quillmere®</h2>
  <div class="intro-copy" style="top:33px">Innovative technology on a highly secure and encrypted platform</div>
  <div class="intro-copy" style="top:50px">An intuitive, gamified user interface</div>
  <div class="intro-copy" style="top:62px;width:145px">Designed for valuation, collaboration, and trading of data assets on the Ledgerline Exchange®</div>
  <div class="glow" style="left:60px;top:100px;width:115px;height:95px" role="img" aria-label="Brand decoration area in green and blue tones"></div>
  <div class="abs" style="left:8px;top:86px;width:111px;height:62px;border-radius:3px;background:linear-gradient(150deg,#2a3444,#0f1722 60%,#1fd08f)" role="img" aria-label="Laptop showing the platform dashboard"></div>
  <div class="shot" style="top:28px;height:47px" role="img" aria-label="Market data screen"></div>
  <div class="shot" style="top:79px;height:47px" role="img" aria-label="Vault wallet screen"></div>
  <div class="shot" style="top:134px;height:27px" role="img" aria-label="Data set merge screen"></div>
  <div class="feature" style="top:41px"><b>Market Data</b>See market data in your vault and visualize market trends</div>
  <div class="feature" style="top:93px"><b>Review Your Vault</b>Track assets in your wallet in real time</div>
  <div class="feature" style="top:135px"><b>Combine Your Data Sets</b>Merge data objects from your wallet to create complimenting data combinations</div>
  <div class="brand brand-sm"><i class="dot"></i>Quillmere AI</div>
</section>

<!-- 5 Text + frame -->
<section class="slide col-l row-3">
  <h2 class="heading">Heading Goes Here</h2>
  <div class="body-copy">
    <p>Lorem ipsum dolor sit amet, consectetuer adipiscing elit, sed diam nonummy nibh euismod tincidunt ut laoreet dolore magna aliquam erat volutpat. Ut wisi enim ad minim veniam, quis nostrud exerci tation ullamcorper suscipit lobortis nisl ut aliquip ex ea commodo consequat. Duis autem vel eum iriure dolor in hendrerit in vulputate velit esse molestie consequat, vel illum dolore eu feugiat nulla facilisis at vero eros et accumsan et iusto odio dignissim qui blandit praesent luptatum zzril delenit augue duis dolore te feugait nulla facilisi.</p>
    <p>Lorem ipsum dolor sit amet, cons ectetuer adipiscing elit, sed diam nonummy nibh euismod tincidunt ut laoreet dolore magna aliquam erat volutpat. Ut wisi enim ad minim veniam, quis nostrud exerci tation ullamcorper suscipit lobortis nisl ut aliquip ex ea commodo consequat.</p>
    <p>Lorem ipsum dolor sit amet, cons ectetuer adipiscing elit, sed diam nonummy nibh euismod tincidunt ut laoreet dolore magna aliquam erat volutpat. Ut wisi enim ad minim veniam, quis nostrud exerci tation ullamcorper suscipit lobortis nisl ut aliquip ex ea commodo consequat.</p>
  </div>
  <div class="frame" style="left:170px;top:37px;width:138px;height:111px"></div>
  <div class="brand brand-sm"><i class="dot"></i>Quillmere AI</div>
</section>

<!-- 6 Text + frame -->
<section class="slide col-r row-3">
  <h2 class="heading">Heading Goes Here</h2>
  <div class="body-copy">
    <p>Lorem ipsum dolor sit amet, consectetuer adipiscing elit, sed diam nonummy nibh euismod tincidunt ut laoreet dolore magna aliquam erat volutpat. Ut wisi enim ad minim veniam, quis nostrud exerci tation ullamcorper suscipit lobortis nisl ut aliquip ex ea commodo consequat. Duis autem vel eum iriure dolor in hendrerit in vulputate velit esse molestie consequat, vel illum dolore eu feugiat nulla facilisis at vero eros et accumsan et iusto odio dignissim qui blandit praesent luptatum zzril delenit augue duis dolore te feugait nulla facilisi.</p>
    <p>Lorem ipsum dolor sit amet, cons ectetuer adipiscing elit, sed diam nonummy nibh euismod tincidunt ut laoreet dolore magna aliquam erat volutpat. Ut wisi enim ad minim veniam, quis nostrud exerci tation ullamcorper suscipit lobortis nisl ut aliquip ex ea commodo consequat.</p>
    <p>Lorem ipsum dolor sit amet, cons ectetuer adipiscing elit, sed diam nonummy nibh euismod tincidunt ut laoreet dolore magna aliquam erat volutpat. Ut wisi enim ad minim veniam, quis nostrud exerci tation ullamcorper suscipit lobortis nisl ut aliquip ex ea commodo consequat.</p>
  </div>
  <div class="frame" style="left:170px;top:37px;width:138px;height:111px"></div>
  <div class="brand brand-sm"><i class="dot"></i>Quillmere AI</div>
</section>

<!-- 7 Text + visual -->
<section class="slide col-l row-4">
  <h2 class="heading">Heading Goes Here</h2>
  <div class="body-copy">
    <p>Lorem ipsum dolor sit amet, consectetuer adipiscing elit, sed diam nonummy nibh euismod tincidunt ut laoreet dolore magna aliquam erat volutpat. Ut wisi enim ad minim veniam, quis nostrud exerci tation ullamcorper suscipit lobortis nisl ut aliquip ex ea commodo consequat. Duis autem vel eum iriure dolor in hendrerit in vulputate velit esse molestie consequat, vel illum dolore eu feugiat nulla facilisis at vero eros et accumsan et iusto odio dignissim qui blandit praesent luptatum zzril delenit augue duis dolore te feugait nulla facilisi.</p>
    <p>Lorem ipsum dolor sit amet, cons ectetuer adipiscing elit, sed diam nonummy nibh euismod tincidunt ut laoreet dolore magna aliquam erat volutpat. Ut wisi enim ad minim veniam, quis nostrud exerci tation ullamcorper suscipit lobortis nisl ut aliquip ex ea commodo consequat.</p>
    <p>Lorem ipsum dolor sit amet, cons ectetuer adipiscing elit, sed diam nonummy nibh euismod tincidunt ut laoreet dolore magna aliquam erat volutpat. Ut wisi enim ad minim veniam, quis nostrud exerci tation ullamcorper suscipit lobortis nisl ut aliquip ex ea commodo consequat.</p>
  </div>
  <div class="frame" style="left:168px;top:33px;width:145px;height:121px;border-width:.9px;background:radial-gradient(circle at 35% 50%,rgba(31,208,143,.45),rgba(20,64,168,.35) 40%,#0b1222 75%)" role="img" aria-label="Isometric data blocks visual in teal and blue"></div>
  <div class="brand brand-sm"><i class="dot"></i>Quillmere AI</div>
</section>

<!-- 8 Line chart -->
<section class="slide col-r row-4">
  <h2 class="heading">Heading Goes Here</h2>
  <div class="chart-title" style="left:13px;top:33px">Line Chart</div>
  <div class="legend" style="right:18px;top:41px"><span><i style="background:var(--blue)"></i>Sales</span><span><i style="background:var(--green)"></i>Orders</span></div>
  <svg class="abs" style="left:10px;top:44px" width="310" height="114" viewBox="0 0 310 114">
    <path d="M11 2H304M11 12H304M11 22H304M11 32H304M11 42H304M11 52H304M11 62H304M11 72H304M11 82H304M11 92H304M11 102H304M11 2V102M35.4 2V102M59.8 2V102M84.3 2V102M108.7 2V102M133.1 2V102M157.5 2V102M181.9 2V102M206.4 2V102M230.8 2V102M255.2 2V102M279.6 2V102M304 2V102" stroke="var(--grid)" stroke-width=".4" fill="none"/>
    <g font-size="2.6" fill="#cfd5de" text-anchor="end">
      <text x="8" y="3">100</text><text x="8" y="13">90</text><text x="8" y="23">80</text><text x="8" y="33">70</text><text x="8" y="43">60</text><text x="8" y="53">50</text><text x="8" y="63">40</text><text x="8" y="73">30</text><text x="8" y="83">20</text><text x="8" y="93">10</text><text x="8" y="103">0</text>
    </g>
    <g font-size="2.6" fill="#cfd5de" text-anchor="middle">
      <text x="23.2" y="109">JAN</text><text x="47.6" y="109">FEB</text><text x="72" y="109">MAR</text><text x="96.5" y="109">APR</text><text x="120.9" y="109">MAY</text><text x="145.3" y="109">JUN</text><text x="169.7" y="109">JUL</text><text x="194.1" y="109">AUG</text><text x="218.6" y="109">SEP</text><text x="243" y="109">OCT</text><text x="267.4" y="109">NOV</text><text x="291.8" y="109">DEC</text>
    </g>
    <polyline fill="none" stroke="var(--green)" stroke-width=".8" points="11,62 35.4,52 59.8,62 84.3,32 108.7,32 133.1,42 157.5,32 181.9,32 206.4,15 230.8,12 255.2,12 279.6,15 304,12"/>
    <polyline fill="none" stroke="var(--blue)" stroke-width=".8" points="11,92 35.4,72 59.8,82 84.3,52 108.7,42 133.1,62 157.5,52 181.9,62 206.4,42 230.8,22 255.2,32 279.6,42 304,22"/>
    <g fill="var(--green)"><circle cx="11" cy="62" r="1.1"/><circle cx="35.4" cy="52" r="1.1"/><circle cx="59.8" cy="62" r="1.1"/><circle cx="84.3" cy="32" r="1.1"/><circle cx="108.7" cy="32" r="1.1"/><circle cx="133.1" cy="42" r="1.1"/><circle cx="157.5" cy="32" r="1.1"/><circle cx="181.9" cy="32" r="1.1"/><circle cx="206.4" cy="15" r="1.1"/><circle cx="230.8" cy="12" r="1.1"/><circle cx="255.2" cy="12" r="1.1"/><circle cx="279.6" cy="15" r="1.1"/><circle cx="304" cy="12" r="1.1"/></g>
    <g fill="var(--blue)"><circle cx="11" cy="92" r="1.1"/><circle cx="35.4" cy="72" r="1.1"/><circle cx="59.8" cy="82" r="1.1"/><circle cx="84.3" cy="52" r="1.1"/><circle cx="108.7" cy="42" r="1.1"/><circle cx="133.1" cy="62" r="1.1"/><circle cx="157.5" cy="52" r="1.1"/><circle cx="181.9" cy="62" r="1.1"/><circle cx="206.4" cy="42" r="1.1"/><circle cx="230.8" cy="22" r="1.1"/><circle cx="255.2" cy="32" r="1.1"/><circle cx="279.6" cy="42" r="1.1"/><circle cx="304" cy="22" r="1.1"/></g>
  </svg>
  <div class="brand brand-sm"><i class="dot"></i>Quillmere AI</div>
</section>

<!-- 9 Stacked chart -->
<section class="slide col-l row-5">
  <h2 class="heading">Heading Goes Here</h2>
  <div class="chart-title" style="left:15px;top:37px">Stacked Chart</div>
  <div class="legend" style="right:20px;top:45px"><span><i style="background:var(--green)"></i>Receipts</span><span><i style="background:var(--green)"></i>Sales</span><span><i style="background:var(--blue)"></i>Orders</span></div>
  <svg class="abs" style="left:8px;top:49px" width="310" height="112" viewBox="0 0 310 112">
    <defs>
      <linearGradient id="base" x1="0" y1="0" x2="0" y2="1"><stop offset="0" stop-color="#1fb88a"/><stop offset="1" stop-color="#1456b8"/></linearGradient>
    </defs>
    <path d="M14 2H304M14 12H304M14 22H304M14 32H304M14 42H304M14 52H304M14 62H304M14 72H304M14 82H304M14 92H304M14 102H304M14 2V102M38.2 2V102M62.3 2V102M86.5 2V102M110.7 2V102M134.8 2V102M159 2V102M183.2 2V102M207.4 2V102M231.5 2V102M255.7 2V102M279.9 2V102M304 2V102" stroke="var(--grid)" stroke-width=".4" fill="none"/>
    <g font-size="2.6" fill="#cfd5de" text-anchor="end">
      <text x="11" y="3">100</text><text x="11" y="13">90</text><text x="11" y="23">80</text><text x="11" y="33">70</text><text x="11" y="43">60</text><text x="11" y="53">50</text><text x="11" y="63">40</text><text x="11" y="73">30</text><text x="11" y="83">20</text><text x="11" y="93">10</text><text x="11" y="103">0</text>
    </g>
    <g fill="url(#base)">
      <rect x="19.1" y="92" width="14" height="10"/><rect x="43.3" y="72" width="14" height="30"/><rect x="67.4" y="89" width="14" height="13"/><rect x="91.6" y="86" width="14" height="16"/><rect x="115.8" y="62" width="14" height="40"/><rect x="139.9" y="89" width="14" height="13"/><rect x="164.1" y="75" width="14" height="27"/><rect x="188.3" y="82" width="14" height="20"/><rect x="212.4" y="89" width="14" height="13"/><rect x="236.6" y="67" width="14" height="35"/><rect x="260.8" y="75" width="14" height="27"/><rect x="284.9" y="89" width="14" height="13"/>
    </g>
    <g fill="var(--blue)">
      <rect x="19.1" y="82" width="14" height="10"/><rect x="43.3" y="42" width="14" height="30"/><rect x="67.4" y="75" width="14" height="14"/><rect x="91.6" y="18" width="14" height="68"/><rect x="115.8" y="42" width="14" height="20"/><rect x="139.9" y="75" width="14" height="14"/><rect x="164.1" y="48" width="14" height="27"/><rect x="188.3" y="62" width="14" height="20"/><rect x="212.4" y="75" width="14" height="14"/><rect x="236.6" y="32" width="14" height="35"/><rect x="260.8" y="49" width="14" height="26"/><rect x="284.9" y="75" width="14" height="14"/>
    </g>
    <g fill="var(--green)">
      <rect x="19.1" y="72" width="14" height="10"/><rect x="43.3" y="12" width="14" height="30"/><rect x="67.4" y="42" width="14" height="33"/><rect x="91.6" y="2" width="14" height="16"/><rect x="115.8" y="22" width="14" height="20"/><rect x="164.1" y="22" width="14" height="26"/><rect x="188.3" y="12" width="14" height="50"/><rect x="212.4" y="52" width="14" height="23"/><rect x="260.8" y="22" width="14" height="27"/><rect x="284.9" y="62" width="14" height="13"/>
    </g>
    <g font-size="2.6" fill="#cfd5de" text-anchor="middle">
      <text x="26.1" y="108">JAN</text><text x="50.3" y="108">FEB</text><text x="74.4" y="108">MAR</text><text x="98.6" y="108">APR</text><text x="122.8" y="108">MAY</text><text x="146.9" y="108">JUN</text><text x="171.1" y="108">JUL</text><text x="195.3" y="108">AUG</text><text x="219.4" y="108">SEP</text><text x="243.6" y="108">OCT</text><text x="267.8" y="108">NOV</text><text x="291.9" y="108">DEC</text>
    </g>
  </svg>
  <div class="brand brand-sm"><i class="dot"></i>Quillmere AI</div>
</section>

<!-- 10 Thank you -->
<section class="slide col-r row-5">
  <div class="brand" style="left:19px;top:18px;font-size:10px"><i class="dot" style="width:8px;height:8px;margin-right:2px"></i>Quillmere AI</div>
  <h2 class="abs thanks">Thank<br><strong>You!</strong></h2>
  <p class="abs thanks-meta">CAPABILITIES<br>PRESENTATION<br>2026</p>
  <div class="glow" style="left:140px;top:30px;width:200px;height:170px" role="img" aria-label="Brand decoration area in green and blue tones"></div>
</section>

</body>
</html>
```